Purchase Protection Subscription Program needs a refreshed website

We are refreshing an existing website www.carevaultplus.example. This is a purchase protection product which allows its members to receive extended warranty on the items they buy, receive a rebate of 50% on a repair of an item, a personal shopping concierge, etc. We are looking for a fresh, clean approach - with mass appeal to both men and woman. The site should convey trust, and ease of use.

Thanks to everyone who posted designs. Amazing work! It was a very difficult decision!

```html
<!DOCTYPE html>
<html lang="en">
<head>
<meta charset="utf-8">
<title>CareVault Plus – Shop with Confidence</title>
<link href="https://fonts.googleapis.com/css2?family=Titillium+Web:wght@300;400;600;700&display=swap" rel="stylesheet">
<style>
:root{
  --red:#c8242c;
  --red-band:#cf3239;
  --orange:#f47a1f;
  --ink:#3a3a3a;
  --muted:#8a8f94;
  --link-blue:#2a9fd8;
  --topbar:#e8ecef;
  --section:#f5f5f5;
  --line:#dcdcdc;
  --dark:#1d1d1d;
}
*{box-sizing:border-box;margin:0;padding:0}
html,body{width:1024px;height:1200px;overflow:hidden}
body{font-family:"Titillium Web",sans-serif;color:var(--ink);background:#fff;position:relative}
.abs{position:absolute}
a{text-decoration:none;color:inherit}

.topbar{left:0;top:0;width:1024px;height:74px;background:var(--topbar)}
.brand{font-size:21px;font-weight:400;color:#1c1c1c;letter-spacing:-.3px}
.brand-top{left:142px;top:14px}
.account-links{top:20px;left:505px;display:flex;font-size:12px;color:var(--muted)}
.account-links a{padding:0 20px;border-left:1px solid #cfd3d6;line-height:14px}
.account-links a:first-child{border:0;padding-left:0}
.btn{display:flex;align-items:center;justify-content:center;border-radius:2px;font-weight:600}
.btn-login{left:706px;top:12px;width:88px;height:31px;background:#fbfbfb;border:1px solid #c9c9c9;color:#666;font-size:12px}
.btn-register{left:800px;top:12px;width:88px;height:31px;background:var(--red);color:#fff;font-size:12px}

.hero{left:0;top:74px;width:1024px;height:368px;background:linear-gradient(90deg,#f1f1f0 0%,#ececea 35%,#c9a08a 58%,#6d5a55 80%,#8a7a6e 100%)}
.hero-photo{left:330px;top:74px;width:694px;height:368px;background:linear-gradient(100deg,rgba(241,241,240,0) 0%,rgba(184,128,100,.55) 35%,rgba(95,80,76,.75) 70%,rgba(150,140,120,.6) 100%)}
.mainnav{left:136px;top:54px;width:752px;height:40px;background:#fff;border:1px solid #d6d6d6;border-radius:2px;box-shadow:0 1px 2px rgba(0,0,0,.06)}
.mainnav a{position:absolute;top:10px;font-size:12px;font-weight:600;color:#6c6c6c}
.hero-title{left:162px;top:188px;font-size:34px;font-weight:700;color:#3b3b3b}
.hero-sub{left:162px;top:236px;font-size:19px;font-weight:300;color:#7d7d7d}
.btn-hero{left:162px;top:293px;width:112px;height:36px;background:var(--red);color:#fff;font-size:13px;font-weight:700}

.features{left:0;top:442px;width:1024px;height:438px;background:var(--section)}
.photo-circle{width:174px;height:174px;border-radius:50%;background:#fff;top:477px}
.divider{top:670px;width:1px;height:159px;background:var(--line)}
.feature{top:672px;width:240px}
.feature h3{display:flex;align-items:center;gap:8px;font-size:13px;font-weight:600;color:#2b2b2b;margin-bottom:12px}
.feature p{font-size:10px;line-height:14.5px;color:var(--muted)}
.feature .lead{font-weight:600;color:#7d8288;margin-bottom:2px}
.ticks{display:grid;grid-template-columns:145px 95px;font-size:10px;line-height:19px;color:var(--muted);list-style:none}
.ticks li{display:flex;gap:5px;align-items:flex-start}
.ticks li svg{margin-top:5px;flex:none}
.hl{color:var(--red);font-weight:700}
.btn-more{top:798px;width:88px;height:32px;background:#fafafa;border:1px solid #c6c6c6;border-radius:2px;font-size:11px;color:#777;display:flex;align-items:center;justify-content:center;box-shadow:0 1px 1px rgba(0,0,0,.08)}

.cta{left:0;top:880px;width:1024px;height:67px;background:var(--red-band)}
.cta-text{left:225px;top:893px;font-size:29px;font-weight:400;color:#fff}
.btn-cta{left:708px;top:898px;width:110px;height:34px;background:var(--orange);color:#fff;font-size:12px;font-weight:700;border-radius:2px}

.footer{left:0;top:947px;width:1024px;height:221px;background:repeating-linear-gradient(135deg,#fff 0 3px,#f6f6f6 3px 4px)}
.brand-foot{left:134px;top:971px}
.fcol{top:975px}
.fcol h4{font-size:11px;font-weight:400;color:#444;margin-bottom:7px}
.fcol a,.fcol div{display:block;font-size:11px;line-height:24px;color:#a0a0a0}
.fcol a.active{color:var(--link-blue)}
.contact-row{display:flex !important;align-items:center;gap:8px;font-size:9px !important;line-height:22px !important;color:#7d8a97 !important}
.social{top:998px;width:26px;height:26px}
.fineprint{left:127px;top:1091px;width:780px;font-size:8.6px;line-height:14.4px;color:#a6a6a6}

.bottombar{left:0;top:1168px;width:1024px;height:32px;background:var(--dark);color:#c9c9c9;font-size:9.5px}
.bottombar span{position:absolute;top:9px}
</style>
</head>
<body>

<div class="abs topbar"></div>
<div class="abs brand brand-top">CareVault Plus</div>
<nav class="abs account-links"><a>Manage</a><a>User</a><a>Profile</a></nav>
<a class="abs btn btn-login">Login</a>
<a class="abs btn btn-register">Register</a>

<div class="abs hero"></div>
<div class="abs hero-photo" role="img" aria-label="Photo of a smiling couple out shopping, carrying shopping bags"></div>
<nav class="abs mainnav">
  <a style="left:29px">Home</a>
  <a style="left:101px">About</a>
  <a style="left:174px">Product Features</a>
  <a style="left:302px">How It Works</a>
  <a style="left:412px">Privacy</a>
  <a style="left:492px">Contact Us</a>
</nav>
<h1 class="abs hero-title">Shop with Confidence</h1>
<p class="abs hero-sub">knowing CareVault Plus is there.</p>
<a class="abs btn btn-hero">Get Started</a>

<section class="abs features"></section>
<div class="abs photo-circle" style="left:169px" role="img" aria-label="Photo of a woman holding a card and shopping bags"></div>
<div class="abs photo-circle" style="left:427px" role="img" aria-label="Photo of a man carrying shopping bags"></div>
<div class="abs photo-circle" style="left:682px" role="img" aria-label="Photo of a happy couple giving thumbs up"></div>
<div class="abs divider" style="left:385px"></div>
<div class="abs divider" style="left:640px"></div>

<div class="abs feature" style="left:138px">
  <h3><svg width="18" height="20" viewBox="0 0 18 20"><path d="M4 9V6a5 5 0 0 1 10 0v3" fill="none" stroke="#c8242c" stroke-width="2.5"/><rect x="1" y="9" width="16" height="11" rx="1" fill="#c8242c"/><circle cx="9" cy="14" r="1.6" fill="#fff"/></svg>Valuable Purchase Protection</h3>
  <p class="lead">Get 5 unique ways to get more out of things you buy:*</p>
  <ul class="ticks">
    <li><svg width="9" height="7" viewBox="0 0 9 7"><path d="M1 3.5l2.5 2.5L8 1" fill="none" stroke="#c8242c" stroke-width="2"/></svg>Warranty extension</li>
    <li><svg width="9" height="7" viewBox="0 0 9 7"><path d="M1 3.5l2.5 2.5L8 1" fill="none" stroke="#c8242c" stroke-width="2"/></svg>Price protection</li>
    <li><svg width="9" height="7" viewBox="0 0 9 7"><path d="M1 3.5l2.5 2.5L8 1" fill="none" stroke="#c8242c" stroke-width="2"/></svg>Repair bill rebate</li>
    <li><svg width="9" height="7" viewBox="0 0 9 7"><path d="M1 3.5l2.5 2.5L8 1" fill="none" stroke="#c8242c" stroke-width="2"/></svg>Restocking fee</li>
    <li><svg width="9" height="7" viewBox="0 0 9 7"><path d="M1 3.5l2.5 2.5L8 1" fill="none" stroke="#c8242c" stroke-width="2"/></svg>Product return guarantee</li>
    <li style="padding-left:14px">reimbursement</li>
  </ul>
</div>
<a class="abs btn-more" style="left:138px">Learn More</a>

<div class="abs feature" style="left:419px;width:200px">
  <h3><svg width="19" height="18" viewBox="0 0 19 18"><path d="M6 5V3a3.5 3.5 0 0 1 7 0v2" fill="none" stroke="#c8242c" stroke-width="2"/><path d="M1 5h17l-1 13H2z" fill="#c8242c"/></svg>Easy Claims Process</h3>
  <p>Using CareVault Plus has never been easier. Just send us copies, scans or photos of your receipts — we’ll store them securely online. Then download what you need and submit your claim online.</p>
</div>
<a class="abs btn-more" style="left:418px">Learn More</a>

<div class="abs feature" style="left:672px;width:215px">
  <h3><svg width="18" height="20" viewBox="0 0 18 20"><path d="M4 9V6a5 5 0 0 1 10 0v3" fill="none" stroke="#c8242c" stroke-width="2.5"/><rect x="1" y="9" width="16" height="11" rx="1" fill="#c8242c"/><circle cx="9" cy="14" r="1.6" fill="#fff"/></svg>One Low Monthly Fee</h3>
  <p>PLUS get a <span class="hl">$5 bonus rebate</span> each calendar quarter to use on home electronics and appliance purchases!*</p>
</div>
<a class="abs btn-more" style="left:672px">Learn More</a>

<div class="abs cta"></div>
<p class="abs cta-text">Start using CareVault Plus today!</p>
<a class="abs btn btn-cta">Get Started Now</a>

<footer class="abs footer"></footer>
<div class="abs brand brand-foot">CareVault Plus</div>
<div class="abs fcol" style="left:400px">
  <h4>Navigation</h4>
  <a class="active">Home</a><a>About Us</a><a>Contact Us</a>
</div>
<div class="abs fcol" style="left:511px">
  <h4>Imporant Links</h4>
  <a>Privacy</a><a>Product Features</a><a>How It Works</a>
</div>
<div class="abs fcol" style="left:638px">
  <h4>Contact</h4>
  <div class="contact-row"><svg width="11" height="11" viewBox="0 0 24 24"><path d="M6.6 10.8a15 15 0 0 0 6.6 6.6l2.2-2.2c.3-.3.7-.4 1-.2 1.1.4 2.3.6 3.6.6.6 0 1 .4 1 1V20c0 .6-.4 1-1 1A17 17 0 0 1 3 4c0-.6.4-1 1-1h3.5c.6 0 1 .4 1 1 0 1.3.2 2.5.6 3.6.1.3 0 .7-.2 1z" fill="#222"/></svg>+1 800 555 0142</div>
  <div class="contact-row"><svg width="11" height="9" viewBox="0 0 22 16"><rect width="22" height="16" rx="1" fill="#222"/><path d="M1 1l10 8 10-8" fill="none" stroke="#fff" stroke-width="1.5"/></svg>info@carevaultplus.example</div>
</div>
<div class="abs fcol" style="left:784px"><h4>Follow Us</h4></div>
<a class="abs social" style="left:786px;background:#3b5b98" aria-label="Social link one"></a>
<a class="abs social" style="left:824px;background:#2aa3de" aria-label="Social link two"></a>
<a class="abs social" style="left:862px;background:#1b6fa3" aria-label="Social link three"></a>

<p class="abs fineprint">*Exclusions and limitations apply. See Terms and Conditions for complete product benefit details. Warranty Extension and Repair Bill Rebate benefits are not available in Maine. Warranty Extension and Repair Bill Rebate benefits are provided by Northfield Product Care Group, except in Arizona, Florida, Oklahoma and Wisconsin, where they are provided by Warrantyline Services, Inc. (License No. 00000), both of which are located at 400 Lakeview Ave., Springfield, IL 62701, (555) 014-2200. The programs are administered by Brightpath Program Solutions, Inc., 400 Lakeview Ave., Springfield, IL 62701, (555) 014-2200. Bonus Rebates are limited to one rebate per purchased item and one purchase per calendar quarter.</p>

<div class="abs bottombar">
  <span style="left:142px">Copyright © 2014 - CareVaultPlus. All rights reserved.</span>
  <span style="left:781px">Privacy Policy</span>
  <span style="left:862px">Sitemap</span>
</div>

</body>
</html>
```